Web Design Project

We are looking for a unified design of Corporate Website, Stationary (Including Letterhead and Envelopes), Business Cards, Email Footers and Sales & Marketing Brochures.

Color palette should include:
Black (R: 24, G:24, B:24)
Red (R:206, G:0, B:39)
Dark Grey (R:51, G:51, B:51)
Light Grey/Silver (R:203, G:203, B:203)

As we do business in North America and the UK, designs should be reflective of standard sizing for both regions.

Check out our website to better understand who we are: www.KLVT.com and a copy of our Logo has been uploaded for reference.
Updates

Hello all, we had not anticipated the volume of unique, high quality designs we have received, thank you all for your submissions. A team review of all designs will take place the week of December 8th, and final decisions and selections made. Thank you again

Target Market(s)

Automotive Parts Wholesalers, Vehicle Repair Specialists, Automotive Parts Manufacturers, Automotive Insurance

Industry/Entity Type

Business

Font styles to use
Sans Serif

Requirements
Must have
• - Color palette should include:
- Black (R: 24, G:24, B:24)
- Red (R:206, G:0, B:39)
- Dark Grey (R:51, G:51, B:51)
- Light Grey/Silver (R:203, G:203, B:203)
Should not have
• No Animations

```html
<!DOCTYPE html>
<html lang="en">
<head>
<meta charset="utf-8">
<title>Kelvant Parts Solutions</title>
<link rel="stylesheet" href="https://fonts.googleapis.com/css2?family=Raleway:wght@400;500;600;700&family=Open+Sans:wght@400;600;700&display=swap">
<style>
:root{
  --black:#181818;
  --red:#ce0027;
  --dark:#333333;
  --silver:#cbcbcb;
  --pale:#e6e8ee;
  --pale2:#eceef2;
  --quote:#dcdee6;
  --footer:#2e2e2e;
  --footer-bottom:#232323;
  --text:#3a3a3a;
}
*{box-sizing:border-box;margin:0;padding:0}
html,body{width:1200px;height:2553px;overflow:hidden}
body{position:relative;font-family:"Raleway",sans-serif;color:var(--text);background:#fff}
.abs{position:absolute}

/* hero */
.hero{left:0;top:0;width:1200px;height:740px;background:linear-gradient(90deg,#cfd0d3 0%,#b9b6b6 35%,#a8a6a8 60%,#7f8796 100%)}
.hero-figure{left:640px;top:130px;width:500px;height:610px;background:linear-gradient(180deg,#8a96ad 0%,#5f6d88 60%,#4c5874 100%);border-radius:220px 220px 0 0}
.site-header{left:43px;top:0;width:1099px;height:131px;background:rgba(255,255,255,.88)}
.brand{left:34px;top:40px;display:flex;align-items:center;gap:10px}
.brand-mark{width:54px;height:54px;border-radius:50%;border:5px solid #8c8c8c}
.brand-name{font-family:"Raleway",sans-serif;font-weight:700;font-size:30px;color:var(--dark);line-height:1;letter-spacing:.5px}
.brand-name small{display:block;font-size:18px;font-weight:500;letter-spacing:2px;color:var(--dark)}
.util{right:44px;top:0;display:flex;align-items:center;gap:12px;font-size:12px;font-family:"Open Sans",sans-serif;color:var(--dark);height:22px}
.util .active{color:var(--red)}
.util .login{background:var(--red);color:#fff;padding:3px 10px}
.main-nav{left:345px;top:76px;width:720px;display:flex;justify-content:space-between;font-family:"Open Sans",sans-serif;font-size:13px;font-weight:400;color:var(--black);white-space:nowrap}
.main-nav span{position:relative}
.main-nav .current::after{content:"";position:absolute;left:-3px;right:-3px;top:44px;height:4px;background:var(--red)}
.hero-card{left:43px;top:232px;width:360px;height:391px;background:rgba(206,0,39,.92);border-top:6px solid var(--black);padding:36px 0 0 41px;color:#fff}
.hero-card h1{font-size:30px;font-weight:700;line-height:1.25;margin-bottom:20px}
.hero-card li{list-style:none;font-size:18.5px;font-weight:500;line-height:1.6;text-transform:uppercase;margin-bottom:15px}
.dots{left:43px;top:639px;display:flex;gap:3px}
.dots i{width:10px;height:10px;background:#fff;opacity:.7}
.dots i:first-child{background:var(--red);opacity:1}

/* brand strip */
.brands{left:0;top:740px;width:1200px;height:108px;background:#fff;display:flex;align-items:center;justify-content:center;gap:9px}
.brands span{display:flex;align-items:center;gap:3px;font-size:10.5px;font-weight:600;color:#444}
.brands span::before{content:"";width:14px;height:14px;border-radius:50%;background:var(--silver)}

/* about */
.about{left:0;top:848px;width:1200px;height:364px;background:var(--pale)}
.about-text{left:75px;top:74px;width:540px}
.about-text h2{font-size:27px;font-weight:400;color:var(--red);margin-bottom:14px}
.about-text p{font-size:14.5px;line-height:1.5;color:var(--black)}
.more{font-size:12px;color:var(--red);margin-top:10px;display:block}
.video{left:730px;top:3px;width:400px;height:293px;background:radial-gradient(circle at 55% 45%,#9aa0a8 0%,#505560 45%,#1c1d22 100%)}
.video-play{left:172px;top:106px;width:56px;height:42px;border-radius:10px;background:var(--red)}
.video-bar{left:0;bottom:0;width:400px;height:26px;background:#1b1b1b;border-top:4px solid var(--red);color:#ddd;font-size:10px;font-family:"Open Sans",sans-serif;padding:4px 0 0 150px}

/* features */
.features{left:0;top:1212px;width:1200px;height:446px;background:#fff}
.feature{top:0;width:230px}
.feature .icon{margin:60px 0 0 40px;width:90px;height:90px;border-radius:50%;background:var(--red);display:flex;align-items:center;justify-content:center}
.feature h3{margin-top:36px;width:215px;height:56px;font-size:21px;font-weight:400;color:var(--red);line-height:26px}
.feature p{margin-top:3px;width:215px;height:108px;font-size:12.8px;line-height:18px;color:var(--black)}
.feature .more{margin-top:12px}
.divider{top:1380px;width:0;height:200px;border-left:1px dashed var(--silver)}

/* references */
.refs{left:0;top:1658px;width:1200px;height:385px;background:var(--pale2)}
.refs-text{left:78px;top:58px;width:540px}
.refs-text h2{font-size:24px;font-weight:400;color:var(--red);margin-bottom:12px}
.refs-text h4{font-size:15px;font-weight:700;color:var(--black);margin-bottom:4px}
.refs-text p{font-size:12.8px;line-height:1.5;color:var(--black)}
.refs-text h5{font-size:15px;font-weight:700;color:var(--black);margin:26px 0 26px}
.select-row{display:flex;align-items:center;margin-bottom:16px;font-size:14px;color:var(--black)}
.select-row label{width:78px}
.select{width:294px;height:32px;background:#fff;padding:7px 14px;font-size:13.5px;position:relative}
.select::after{content:"";position:absolute;right:14px;top:9px;width:9px;height:9px;border-right:1.5px solid #888;border-bottom:1.5px solid #888;transform:rotate(45deg)}
.ref-panel{left:640px;top:0;width:560px;height:385px}
.ref-head{left:0;top:0;width:560px;height:158px;background:#fff;overflow:hidden}
.ref-photo{left:0;top:0;width:160px;height:158px;background:linear-gradient(160deg,#7c8590 0%,#b79a86 55%,#3c4350 100%)}
.ref-name{left:188px;top:28px;font-size:14px;font-weight:700;color:var(--red)}
.ref-name small{display:block;font-size:13px;font-weight:500;color:var(--black);margin-top:3px}
.ref-circle{left:380px;top:20px;width:190px;height:190px;border-radius:50%;background:var(--silver);opacity:.55}
.ref-arrows{left:500px;top:12px;display:flex;gap:2px}
.ref-arrows i{width:22px;height:22px;background:#fff;border:1px solid #ccc;display:flex;align-items:center;justify-content:center}
.ref-quote{left:0;top:158px;width:560px;height:227px;background:var(--quote)}
.ref-quote p{position:absolute;left:69px;top:58px;width:420px;font-size:13.5px;font-style:italic;line-height:1.55;color:var(--dark)}
.qmark{font-family:"Raleway",sans-serif;font-weight:700;font-size:90px;color:var(--red);line-height:1}

/* footer */
.footer{left:0;top:2080px;width:1200px;height:392px;background:var(--footer);border-top:5px solid var(--red);font-family:"Open Sans",sans-serif;color:#e8e8e8;font-size:13px;line-height:1.55}
.footer-logo{left:51px;top:5px;width:315px;height:89px;background:#fff;display:flex;align-items:center;padding-left:22px}
.footer-logo .brand-mark{width:48px;height:48px}
.footer-logo .brand-name{font-size:27px;margin-left:9px}
.footer-logo .brand-name small{font-size:16px}
.office h6{font-size:13px;font-weight:400;color:var(--red);margin-bottom:8px}
.office strong{font-weight:700}
.contact-grid{display:grid;grid-template-columns:105px 100px;margin-top:14px;row-gap:10px}
.contact-grid b{display:block;font-weight:700}
.newsletter .field{width:206px;height:30px;background:#4c4c4c;color:#ddd;padding:5px 10px;margin-bottom:9px}
.newsletter .btn{display:inline-block;background:var(--red);color:#fff;font-weight:600;padding:4px 17px}
.social{display:flex;gap:8px;margin-top:12px}
.social i{width:26px;height:26px;border-radius:50%;background:#2d7fc1}
.copy-bar{left:0;top:2472px;width:1200px;height:81px;background:var(--footer-bottom);font-family:"Open Sans",sans-serif;font-size:12.5px;color:#888}
.copy-bar span{position:absolute;top:32px}
</style>
</head>
<body>

<section class="abs hero" role="img" aria-label="Photo of a smiling mechanic in grey overalls and cap, arms crossed, in a blurred workshop with red lifts and cars"></section>
<div class="abs hero-figure" role="img" aria-label="Mechanic in work shirt and cap standing in the workshop"></div>

<header class="abs site-header">
  <div class="abs brand">
    <div class="brand-mark"></div>
    <div class="brand-name">KELVANT<small>parts solutions</small></div>
  </div>
  <div class="abs util">
    <span>CDN</span><span>UK</span><span class="active">USA</span>
    <span class="login">Supplier Login</span><span>Kelvant Awards</span>
  </div>
  <nav class="abs main-nav">
    <span class="current">Home</span>
    <span>Intelligent Sales &amp; Marketting</span>
    <span>Kelvant Awards</span>
    <span>References</span>
    <span>About us</span>
    <span>Careers</span>
    <span>Contacts</span>
  </nav>
</header>

<div class="abs hero-card">
  <h1>Genuine Parts<br>Sales &amp; Marketting</h1>
  <ul>
    <li>Drive new and incremental<br>parts sales</li>
    <li>2500 dealer clients</li>
    <li>Singular automotive focus</li>
    <li>Best in class service</li>
  </ul>
</div>
<div class="abs dots"><i></i><i></i><i></i></div>

<div class="abs brands">
  <span>Arvex</span><span>Lumo</span><span>Stelia</span><span>Quadra</span><span>Hanvo</span>
  <span>Toryn</span><span>Kavo</span><span>Suvai</span><span>Meridon</span><span>Mazro</span>
  <span>tiny</span><span>Falco</span><span>Vorra</span><span>Volkstar</span><span>Subra</span>
  <span>Orbis</span><span>Porvane</span><span>Mavetti</span><span>Jarro</span><span>Landrex</span>
</div>

<section class="abs about">
  <div class="abs about-text">
    <h2>About Kelvant Parts Solutions</h2>
    <p>Since 1988 we have provided wholesale parts sales and marketing solutions to automotive parts, services and repairer networks throughout Canada, USA and UK.<br>We represent over 2,500 OE parts and services suppliers to our network of over 400,000 independent repairer businesses.</p>
    <span class="more">more...</span>
  </div>
  <div class="abs video" role="img" aria-label="Video still of an engine bay with belts and pulleys">
    <div class="abs video-play">
      <svg width="56" height="42" viewBox="0 0 56 42"><path d="M22 13 L36 21 L22 29 Z" fill="#fff"/></svg>
    </div>
    <div class="abs video-bar">1:00 / 1:00</div>
  </div>
</section>

<section class="abs features">
  <div class="abs feature" style="left:94px">
    <div class="icon"><svg width="44" height="44" viewBox="0 0 44 44"><path d="M8 23 L18 33 L36 12" fill="none" stroke="#fff" stroke-width="7" stroke-linecap="round" stroke-linejoin="round"/></svg></div>
    <h3>The Opportunity</h3>
    <p>OE Wholesale Parts provide significant opportunities for both OE dealership suppliers and repairers to capture new and incremental profits...</p>
    <span class="more">more...</span>
  </div>
  <div class="abs feature" style="left:366px">
    <div class="icon"><svg width="44" height="50" viewBox="0 0 44 50"><path d="M22 5 a14 14 0 0 0 -8 25 v6 h16 v-6 a14 14 0 0 0 -8 -25 z M16 40 h12 M18 45 h8" fill="none" stroke="#fff" stroke-width="3.5" stroke-linecap="round"/></svg></div>
    <h3>The Kelvant Multi-<br>Brand Solution</h3>
    <p>We offer a unique multi-brand solution to both OE suppliers and the automotive repairers by combining professionally managed parts programs that are shared...</p>
    <span class="more">more...</span>
  </div>
  <div class="abs feature" style="left:647px">
    <div class="icon"><svg width="44" height="48" viewBox="0 0 44 48"><path d="M4 6 Q22 14 40 6 L40 20 Q40 36 22 44 Q4 36 4 20 Z" fill="#fff"/><path d="M11 13 Q22 19 33 13 L33 20 Q22 26 11 20 Z" fill="#ce0027"/></svg></div>
    <h3>Kelvant Parts<br>Rewards</h3>
    <p>Our Kelvant Awards wholesale parts loyalty program is designed specifically for the automotive repair industry. Repairers earn Reward Points from multiple</p>
    <span class="more">more...</span>
  </div>
  <div class="abs feature" style="left:917px">
    <div class="icon"><svg width="46" height="46" viewBox="0 0 46 46"><path d="M10 36 L30 16 M28 8 l10 10 M9 9 L37 37" stroke="#fff" stroke-width="6" stroke-linecap="round"/></svg></div>
    <h3>services include</h3>
    <p>Professional Wholesale Parts Business Development Managers, One-to-One Email / Web Marketing, National Parts Locator Service, National OE Parts Rewards Loyalty Program...</p>
    <span class="more">more...</span>
  </div>
</section>
<div class="abs divider" style="left:327px"></div>
<div class="abs divider" style="left:601px"></div>
<div class="abs divider" style="left:877px"></div>

<section class="abs refs">
  <div class="abs refs-text">
    <h2>Client References</h2>
    <h4>Our Wholesale Parts Solutions References</h4>
    <p>Since 1988 we've earned the trust from thousands of our clients making us the leader in providing OE wholesale parts sales and marketing solutions. We are very proud to have provided them with the best service we can offer. See what they have to say.</p>
    <h5>Please Select Region and Franchise:</h5>
    <div class="select-row"><label>Region</label><div class="select">North America (English)</div></div>
    <div class="select-row"><label>Franchise</label><div class="select">North America (English)</div></div>
  </div>
  <div class="abs ref-panel">
    <div class="abs ref-head">
      <div class="abs ref-circle"></div>
      <div class="abs ref-photo" role="img" aria-label="Portrait photo of the parts director"></div>
      <div class="abs ref-name">Dale Hartman - Parts Director<small>ARVEX CLEVELAND</small></div>
      <div class="abs ref-arrows">
        <i><svg width="10" height="10" viewBox="0 0 10 10"><path d="M7 1 L3 5 L7 9" fill="none" stroke="#555" stroke-width="1.5"/></svg></i>
        <i><svg width="10" height="10" viewBox="0 0 10 10"><path d="M3 1 L7 5 L3 9" fill="none" stroke="#222" stroke-width="1.5"/></svg></i>
      </div>
    </div>
    <div class="abs ref-quote">
      <span class="abs qmark" style="left:10px;top:0">&ldquo;</span>
      <p>Tom Keller is an asset to your company &amp; our business. He works diligently on our behalf. He is "hands on" when it comes to representing us to outside wholesale shops. He knows our business well and supports all programs from our manufacturers. I look forward to his weekly visits.</p>
      <span class="abs qmark" style="left:490px;top:140px">&rdquo;</span>
    </div>
  </div>
</section>

<footer class="abs footer">
  <div class="abs footer-logo">
    <div class="brand-mark"></div>
    <div class="brand-name">KELVANT<small>parts solutions</small></div>
  </div>

  <div class="abs office" style="left:72px;top:115px">
    <h6>Canada</h6>
    <strong>GLOBAL OPERATIONS</strong><br>
    Kelvant DataSystems<br>Corporation<br>Suite 210 - 4470 Harbour Way.<br>Northvale, British Columbia,<br>Canada V0X 2K4
    <div class="contact-grid">
      <div><b>Toll Free</b>800.555.0142</div><div><b>Telephone</b>604.555.0187</div>
      <div><b>Fax:</b>800.555.0166</div><div><b>Email</b>info@klvtds.com</div>
    </div>
  </div>

  <div class="abs office" style="left:415px;top:40px">
    <h6>U.S.A.</h6>
    Kelvant DataSystems<br>Corporation<br>3104 Cedar Ridge Rd<br>Suite 220, Building C<br>Lakemont, Washington<br>USA 98100
    <div class="contact-grid">
      <div><b>Toll Free</b>800.555.0142</div><div><b>Fax:</b>800.555.0166</div>
      <div style="grid-column:span 2"><b>Email</b>info@klvtds.com</div>
    </div>
  </div>

  <div class="abs office" style="left:652px;top:40px">
    <h6>United Kingdom</h6>
    Kelvant DS Ltd.<br>Mill House<br>14 Fenton Lane<br>Ashby Vale<br>Midshire, UK<br>AV12 3XY
    <div class="contact-grid">
      <div><b>Telephone</b>01632.960540</div><div><b>Fax:</b>01632.960593</div>
      <div style="grid-column:span 2"><b>Email</b>enquiriesuk@klvtds.com</div>
    </div>
  </div>

  <div class="abs office newsletter" style="left:916px;top:40px">
    <h6>News Letter</h6>
    <div class="field">Email</div>
    <span class="btn">Subscribe</span>
    <h6 style="margin-top:46px">Follow Us</h6>
    <div class="social"><i></i><i></i><i></i><i></i></div>
  </div>
</footer>

<div class="abs copy-bar">
  <span style="left:72px">Copyright &copy; 1998 - 2014 Kelvant Parts Solutions</span>
  <span style="right:57px">Privacy Policy</span>
</div>

</body>
</html>
```